HomePage Design for Lumen Getaways - once-in-a-lifetime experiences for busy working people

Design a homepage for the Lumen Getaways (www.lumengetaways.example) website compatible with further web pages and the design briefing documents attached

LG HomePage Design Brief
We are seeking website HomePage designs incorporating our new Logo and colour scheme, for Lumen Getaways (www.lumengetaways.example) to go with the site functionality and wireframe ideas attached.
The website HomePage design needs to
• Incorporate and be consistent with the LG Logo and its colour scheme attached.
• Express the brand values of being inspirational, high quality, upscale, cultured, aspirational, and contemporary – even somewhat ‘hip’. Probably positioned somewhere between Harlow Pike (Deluxe Travel) and Green Walrus (Hip Travel) – see https://www.harlowpike.example and https://www.greenwalrus.example .
• Be instantly recognisable and different from other travel websites and instantly communicate the nature of the brand proposition and target customer base.
• Appeal to our core 25-55 affluent businesspeople demographic
• Work in the UK, US/Canada and Australia/NZ and ultimately in mainland Europe.
• Use fonts and colours that are easily reproduced online and compatible with nearly all browsers.
• Be part of a responsive website design, that can be used both on Desktops and laptops but also with tablets and mobile ‘phones (hence content not too wide across the page)
• Feature the strapline ‘Lumen Getaways in less than 7 Days’
• Work with the and wireframes and processes shown in the attached presentation – although intended as a guide only these features and processes all need to be incorporated into the HomePage.
• Make full use of high quality images and video to convey our brand proposition and products

Target Market(s)

25-55 affluent businesspeople

Industry/Entity Type

Travel Industry

Number of Pages Required

1 page

Font styles to use
Sans Serif

Colors
0455a3
00a88f

Requirements
Must have
• • Incorporate and be consistent with the LG Logo and its colour scheme attached.
• • Express the brand values of being inspirational, high quality, upscale, cultured, aspirational, and contemporary – even somewhat ‘hip’. Probably positioned somewhere between Harlow Pike (Deluxe Travel) and Green Walrus (Hip Travel) – see https://www.harlowpike.example and https://www.greenwalrus.example .
• • Be instantly recognisable and different from other travel websites and instantly communicate the nature of the brand proposition and target customer base.
• • Appeal to our core 25-55 affluent businesspeople demographic
• • Be part of a responsive website design, that can be used both on Desktops and laptops but also with tablets and mobile ‘phones (hence content not too wide across the page)
• • Feature the strapline ‘Lumen Getaways in less than 7 Days’
• • Work with the and wireframes and processes shown in the attached presentation – although intended as a guide only these features and processes all need to be incorporated into the HomePage.
• • Make full use of high quality images and video to convey our brand proposition and products
• Colours as per Logo not as shown below
Nice to have
• • Work in the UK, US/Canada and Australia/NZ and ultimately in mainland Europe.
Should not have
• Must not be cheap or mass-market, nor excessively "stuffy or luxury-orientated"

```html
<!DOCTYPE html>
<html lang="en">
<head>
<meta charset="utf-8">
<title>Lumen Getaways — Homepage</title>
<link rel="stylesheet" href="https://fonts.googleapis.com/css2?family=Montserrat:wght@400;500;600;700;800&display=swap">
<style>
  :root {
    --ink: #1c1c1c;
    --bar: #1e1e1e;
    --white: #ffffff;
    --brand-green: #2e6b3c;
    --caption-green: #1f5535;
    --muted: #e8e8e8;
    --page: #ffffff;
  }
  * { box-sizing: border-box; margin: 0; padding: 0; }
  html, body { width: 1200px; height: 2284px; overflow: hidden; background: var(--page); }
  body { font-family: "Montserrat", Arial, sans-serif; color: var(--ink); position: relative; }

  .site-header { position: absolute; left: 0; top: 0; width: 1200px; height: 99px; background: var(--white); }
  .brand { position: absolute; left: 0; width: 1200px; top: 30px; display: flex; justify-content: center; align-items: center; gap: 10px; }
  .brand-dot { width: 26px; height: 26px; border-radius: 50%; background: var(--brand-green); }
  .brand-name { font-size: 17px; font-weight: 700; letter-spacing: 1.5px; color: var(--brand-green); }
  .social { position: absolute; left: 991px; top: 0; width: 131px; height: 46px; background: var(--bar); display: flex; align-items: center; justify-content: center; gap: 10px; }
  .social span { width: 14px; height: 14px; border-radius: 50%; background: var(--white); }

  .main-nav { position: absolute; left: 0; top: 99px; width: 1200px; height: 40px; background: var(--bar); }
  .main-nav a { position: absolute; top: 0; height: 40px; line-height: 40px; transform: translateX(-50%); color: var(--white); text-decoration: none; font-size: 11px; font-weight: 500; text-transform: uppercase; white-space: nowrap; }
  .main-nav a.active { background: var(--brand-green); width: 110px; text-align: center; font-weight: 700; }

  .hero { position: absolute; left: 0; top: 139px; width: 1200px; height: 536px;
    background: radial-gradient(ellipse at 68% 22%, #f0b45a 0%, #b0702f 18%, #5c4424 45%, #3a3320 70%, #26241a 100%); }
  .hero-title { position: absolute; left: 148px; top: 208px; color: var(--white); font-size: 35px; font-weight: 800; letter-spacing: 2.5px; line-height: 46px; text-transform: uppercase; }
  .scroll-cue { position: absolute; left: 0; width: 1200px; top: 485px; display: flex; justify-content: center; align-items: center; gap: 14px; color: var(--white); font-size: 10px; font-weight: 600; text-transform: uppercase; }
  .scroll-cue::before, .scroll-cue::after { content: ""; width: 90px; height: 1px; background: rgba(255,255,255,.5); }

  .tile { position: absolute; overflow: hidden; }
  .tile-label { position: absolute; left: 37px; bottom: 24px; color: var(--white); font-size: 21px; font-weight: 700; line-height: 27px; text-transform: uppercase; }
  .tile-wildlife   { left: 0;   top: 675px; width: 300px; height: 386px; background: linear-gradient(160deg, #4f5a46, #2d3226 70%, #3a3f33); }
  .tile-festivals  { left: 300px; top: 675px; width: 300px; height: 386px; background: linear-gradient(150deg, #3d6a86, #9a9a4a 45%, #8e7a8a 70%, #2d3030); }
  .tile-activities { left: 600px; top: 675px; width: 300px; height: 386px; background: linear-gradient(180deg, #4b4f55, #8d9197 55%, #aeb2b6); }
  .tile-events     { left: 900px; top: 675px; width: 300px; height: 386px; background: radial-gradient(circle at 45% 22%, #ff6a2a 0%, #c23a12 14%, #2a1a14 40%, #141210 100%); }
  .tile-secret     { left: 0;   top: 1061px; width: 390px; height: 389px; background: linear-gradient(180deg, #2a2d2e, #3b4336 55%, #23281f); }
  .tile-performances { left: 390px; top: 1048px; width: 413px; height: 417px; z-index: 2; background: radial-gradient(ellipse at 52% 18%, #fff1c8 0%, #f3a142 16%, #5a2f14 42%, #161412 75%); }
  .tile-hiking     { left: 803px; top: 1061px; width: 397px; height: 389px; background: linear-gradient(180deg, #57778f, #748a82 40%, #4e5f43 75%, #3b4833); }

  .last-places { position: absolute; left: 0; top: 1530px; width: 1200px; text-align: center; }
  .section-title { font-size: 20px; font-weight: 500; letter-spacing: .5px; text-transform: uppercase; color: var(--ink); }
  .offer { position: absolute; top: 59px; width: 262px; }
  .offer-image { width: 262px; height: 284px; }
  .offer-caption { margin-top: 12px; font-size: 15px; font-weight: 700; color: var(--caption-green); text-transform: uppercase; white-space: nowrap; }
  .offer-venice { left: 187px; }
  .offer-venice .offer-image { background: linear-gradient(180deg, #d6d4d2 0%, #b49a86 35%, #7a6a5c 65%, #9aa6ae 100%); }
  .offer-island { left: 469px; }
  .offer-island .offer-image { background: linear-gradient(180deg, #3f7fbf 0%, #7eb0dc 50%, #2a2a2a 68%, #4a5a3a 100%); }
  .offer-dead { left: 749px; }
  .offer-dead .offer-image { background: radial-gradient(ellipse at 50% 45%, #cfc8d6 0%, #6a5a8a 30%, #1a1a22 65%); }

  .site-footer { position: absolute; left: 0; top: 2004px; width: 1200px; height: 280px; background: var(--bar); color: var(--white); }
  .footer-col { position: absolute; top: 42px; list-style: none; }
  .footer-col li { font-size: 12.5px; line-height: 17px; margin-bottom: 10px; text-transform: uppercase; }
  .col-1 { left: 149px; } .col-2 { left: 324px; } .col-3 { left: 518px; } .col-4 { left: 731px; width: 150px; } .col-5 { left: 918px; width: 160px; }
  .partner-row { position: absolute; left: 149px; top: 229px; display: flex; gap: 36px; font-size: 18px; font-weight: 500; }
  .copyright { position: absolute; left: 868px; top: 234px; font-size: 12px; }
</style>
</head>
<body>
  <header class="site-header">
    <div class="brand"><span class="brand-dot"></span><span class="brand-name">LUMEN GETAWAYS</span></div>
    <div class="social" aria-label="Social links"><span></span><span></span><span></span><span></span><span></span></div>
  </header>

  <nav class="main-nav">
    <a class="active" style="left:203px">Destinations</a>
    <a style="left:315px">Experiences</a>
    <a style="left:434px">Trips by month</a>
    <a style="left:550px">Topical now</a>
    <a style="left:649px">Tailored</a>
    <a style="left:748px">Pioneers club</a>
    <a style="left:867px">Client log-in</a>
    <a style="left:988px">Vlogs &amp; reviews</a>
  </nav>

  <section class="hero" role="img" aria-label="Winding road through green hills at sunset">
    <h1 class="hero-title">Lumen Getaways<br>in less than 7 days!</h1>
    <div class="scroll-cue">Scroll down</div>
  </section>

  <div class="tile tile-wildlife" role="img" aria-label="Stag grazing in a meadow"><span class="tile-label">Wonders of<br>wildlife</span></div>
  <div class="tile tile-festivals" role="img" aria-label="Crowd in coloured powder at a festival"><span class="tile-label">World's<br>greatest festivals</span></div>
  <div class="tile tile-activities" role="img" aria-label="Dog sled on a snowy trail"><span class="tile-label">Must do<br>activies</span></div>
  <div class="tile tile-events" role="img" aria-label="Sky lantern released at night"><span class="tile-label">Unique<br>annual events</span></div>
  <div class="tile tile-secret" role="img" aria-label="Dark mountain ridge under cloud"><span class="tile-label">Extraordinary<br>and secret places</span></div>
  <div class="tile tile-performances" role="img" aria-label="Fire breather performing at night"><span class="tile-label">Unforgettable<br>performances</span></div>
  <div class="tile tile-hiking" role="img" aria-label="Hiker on a mountain ridge"><span class="tile-label">Spectacular hiking,<br>climbing and walking</span></div>

  <section class="last-places">
    <h2 class="section-title">Last few places</h2>
    <div class="offer offer-venice"><div class="offer-image" role="img" aria-label="Venice canal with gondolas"></div><p class="offer-caption">Venice Carnival £599pp</p></div>
    <div class="offer offer-island"><div class="offer-image" role="img" aria-label="Stone statues on Easter Island"></div><p class="offer-caption">Easter Island £2,999pp</p></div>
    <div class="offer offer-dead"><div class="offer-image" role="img" aria-label="Day of the Dead costume with flower hat"></div><p class="offer-caption">Day of the Dead £3,299pp</p></div>
  </section>

  <footer class="site-footer">
    <ul class="footer-col col-1"><li>About us</li><li>Our partners</li><li>Newsletter</li><li>FAQs</li></ul>
    <ul class="footer-col col-2"><li>Contact us</li><li>Booking conditions</li><li>Privacy &amp; cookies</li><li>Terms of use</li></ul>
    <ul class="footer-col col-3"><li>Financial protection</li><li>Travel insurance</li><li>Visas</li><li>Travel advice</li></ul>
    <ul class="footer-col col-4"><li>Group bookings</li><li>Tailor-made &amp; extra nights</li><li>Booking flights</li><li>Careers with LG</li></ul>
    <ul class="footer-col col-5"><li>LG protecting wildlife &amp; animals, and supporting local communities</li><li>Press room</li></ul>
    <div class="partner-row"><span>LOGO1</span><span>LOGO2</span><span>LOGO3</span><span>LOGO4</span></div>
    <p class="copyright">(c) 2017 Lumen Getaways</p>
  </footer>
</body>
</html>
```